Business Card Design

We need a basic, but modern design card. Our business is a local Queanbeyan/Canberra courier service, but can organise interstate delivery if needed. Our fleet ranges from 1 tonne vans to 8 tonne trucks.

Industry/Entity Type

Business

Contact Information for Business Card

Harbourline Freight
14 Wren Parade
Queanbeyan NSW 2620

Dean Fairley
CEO

Phone: 02 61847315
Fax: 02 61847358
email: dean@harbourlinefreight.example.au

```html
<!DOCTYPE html>
<html lang="en">
<head>
<meta charset="utf-8">
<title>Harbourline Freight – Business Card</title>
<link rel="stylesheet" href="https://fonts.googleapis.com/css2?family=Arimo:wght@400&display=swap">
<style>
  :root {
    --page-bg: #f2f2f2;
    --card-bg: #ffffff;
    --ink: #1d1d1b;
    --brand-blue: #0a6ab7;
    --brand-yellow: #f9b52a;
  }
  html, body {
    margin: 0;
    width: 1200px;
    height: 1000px;
    overflow: hidden;
    background: var(--page-bg);
    font-family: "Arimo", Arial, sans-serif;
  }
  .card {
    position: absolute;
    left: 220px;
    top: 290px;
    width: 742px;
    height: 410px;
    background: var(--card-bg);
    color: var(--ink);
    overflow: hidden;
  }
  .brand-name {
    position: absolute;
    left: 101px;
    top: 150px;
    width: 200px;
    margin: 0;
    font-size: 36px;
    line-height: 40px;
    font-weight: 400;
    color: var(--brand-blue);
    letter-spacing: -0.5px;
  }
  .brand-mark {
    position: absolute;
    left: 103px;
    top: 242px;
    width: 16px;
    height: 16px;
    background: var(--brand-yellow);
  }
  .holder {
    position: absolute;
    left: 398px;
    top: 26px;
    margin: 0;
    font-size: 16px;
    line-height: 20px;
  }
  .contact {
    position: absolute;
    left: 398px;
    top: 178px;
    margin: 0;
    font-style: normal;
    font-size: 16px;
    line-height: 20.6px;
  }
  .edge-stripe {
    position: absolute;
    left: 0;
    bottom: 0;
    width: 742px;
    height: 8px;
    display: flex;
  }
  .edge-stripe .stripe-yellow { flex: 0 0 678px; background: var(--brand-yellow); }
  .edge-stripe .stripe-blue { flex: 1; background: var(--brand-blue); }
</style>
</head>
<body>
  <section class="card">
    <h1 class="brand-name">Harbourline<br>Freight</h1>
    <span class="brand-mark"></span>
    <p class="holder">Dean Fairley CEO</p>
    <address class="contact">
      14 Wren Parade<br>
      Queanbeyan NSW 2620<br>
      Phone: 02 61847315<br>
      Fax: 02 61847358<br>
      email: dean@harbourlinefreight.example.au
    </address>
    <div class="edge-stripe"><span class="stripe-yellow"></span><span class="stripe-blue"></span></div>
  </section>
</body>
</html>
```